Velvet Crest Car Detailing Brochure

I would like a trifold brochure designed for my car detailing business. The background has to be full black or mostly black with some designing using only colors present in our logo.

Front page must have our logo and name, list of services, a photo and mybe our phone number but no long text.

Inside I want to present each service one by one with its description and a photo representing/showing each service. (I will provide the text below). For photos, use stock photos and I will add come of mines already too.

On the back of the brochure I want to have contact & info: phone number, opening hours, address, website, Instagram.

Outside left I want the text About us and photo/design.

I want the brochure to be neat, professional, easy to read, but at the same time not too boring.

Text:
1. About us
a. the ultimate destination for car care in Geneva. We provide personalized, detail-oriented services that bring out the best in your car. With our expert techniques and dedicated approach, we ensure that your car receives the utmost care and attention. Experience a place where passion meets precision and let us create an exceptional car care experience designed just for you.
2. Services:

DETAILING & HAND WASH

• Comprehensive exterior & interior care
• Personalisation and tailored cleaning packages
• Decontamination
• Premium products
• Attention to detail for a perfect finish

POLISHING

• Eliminates scratches, holograms
• Revives and protects paint
• Ensures lasting gloss
• Enhances paint life
• Preserves car’s value and beauty

CERAMIC TREATMENT

• Durable paint protection
• Water-repellent (hydrophobic) effect
• Easier cleaning, enhanced shine
• Long-term surface safeguarding
• Shields against environmental impacts

DRY ICE WASH

• Innovative, waterless method
• Safe for all car parts
• Deep cleans, removes odors
• Allergen-free, antibacterial
• Gentle, effective
• Advanced cleaning technology

COVERING

• Personalized vehicle styling
• More than 150 colours available
• Clean cut without using a cutter
• High-quality, durable materials
• Custom designs available

PROTECTION FILM

• Invisible, durable shield
• Self-healing technology
• 10-year warranty by QR VONT

DETAILING BOUTIQUE

• Premium brands available
• Buy on site during your visit
• Marble Harbour, Zeb Autos, DRUP Polaro
• Essential for at-home car care
• Perfect for quick touch-ups
(for these three brands you can put their logos

Target Market(s)

Our target market includes car owners of all price ranges, with a special focus on those who are passionate about their vehicles. We cater to clients who value excellent service and results, and seek to maintain their cars in pristine condition.

Industry/Entity Type

Automobile / Car detailing

Colors

Designer to choose colors to be used in the design.

Requirements
Must have
• Brand Consistency: The brochure must adhere to our brand colors and style, particularly utilizing the colors present in our logo. Trifold Layout: The design must be specifically tailored for a trifold brochure format. Legibility: Text must be easy to read against the mostly black background, with appropriate font size and style. Professional Look and Feel: The overall design must convey professionalism while being engaging and not overly complex. Photo representation: each service description should have a phot presenting it.
Should not have
• Overcrowded Design: Avoid cluttering with too much text or too many images. The layout should be clean and easy to navigate. Cartoonish Fonts or Graphics: Avoid using unprofessional or casual fonts and graphics that do not align with the upscale and professional image of our business. Distracting Backgrounds: The background should complement and not overpower the content. Stick to the theme of mostly black with design elements from our logo.

```html
<!DOCTYPE html>
<html lang="en">
<head>
<meta charset="utf-8">
<title>Velvet Crest Car Detailing – Trifold Brochure</title>
<link href="https://fonts.googleapis.com/css2?family=Lato:wght@400;700;900&family=Rubik:wght@300;400;500&display=swap" rel="stylesheet">
<style>
:root{
  --page:#efecd9;
  --shadow:#8c8c8c;
  --black:#0a0a0c;
  --panel-light:#1b1b1e;
  --white:#ffffff;
  --magenta:#e0237f;
  --violet:#cf1fe6;
  --purple:#8a46f0;
  --blue:#4ba9f2;
  --label:#5b34b8;
}
*{margin:0;padding:0;box-sizing:border-box}
html,body{width:872px;height:1200px;overflow:hidden;background:var(--page)}
body{font-family:"Lato",sans-serif;color:var(--white);position:relative}
.sheet{position:absolute;width:633px;height:448px;background:var(--black);overflow:hidden}
.sheet--outside{left:124px;top:79px;box-shadow:8px 8px 0 var(--shadow)}
.sheet--inside{left:118px;top:645px;box-shadow:9px 9px 0 var(--shadow)}
.panel{position:absolute;top:0;width:211px;height:448px;background:linear-gradient(90deg,var(--black) 0%,var(--black) 70%,var(--panel-light) 100%)}
.panel--1{left:0}.panel--2{left:211px}.panel--3{left:422px;width:211px;background:var(--black)}
.art{position:absolute;left:0;top:0}
.abs{position:absolute}

/* outside */
.mini-brand{left:0;width:211px;top:36px;text-align:center}
.mini-brand .ring{width:40px;height:40px;border:2px solid var(--purple);border-radius:50%;margin:0 auto 4px}
.mini-brand p{font-family:"Rubik",sans-serif;font-weight:300;font-size:9px;line-height:10.5px;letter-spacing:.3px}
.about-title{left:0;width:211px;top:121px;text-align:center;font-weight:700;font-size:17.5px;color:var(--magenta)}
.about-text{left:22px;width:167px;top:145px;text-align:center;font-size:6.8px;line-height:17.2px;text-transform:uppercase}
.contact{left:264px;top:60px;font-family:"Rubik",sans-serif;font-size:12.6px}
.contact li{list-style:none;display:flex;align-items:center;height:19px}
.contact svg{width:9px;height:9px;margin-right:7px;flex:none}
.address{left:264px;top:136px;font-family:"Rubik",sans-serif;font-size:12.6px;line-height:15px;display:flex}
.address svg{width:10px;height:12px;margin-right:6px;margin-top:1px;flex:none}
.hours{left:211px;width:211px;top:228px;text-align:center}
.hours h3{font-weight:700;font-size:13.5px;letter-spacing:.2px}
.hours p{font-family:"Rubik",sans-serif;font-weight:300;font-size:19.5px;color:var(--violet);line-height:20px;letter-spacing:.5px}
.brand{left:422px;width:211px;top:43px;text-align:center}
.brand .ring{width:100px;height:100px;border:3px solid var(--purple);border-radius:50%;margin:0 auto 8px}
.brand p{font-family:"Rubik",sans-serif;font-weight:400;font-size:21px;line-height:24px;letter-spacing:.6px}
.services-box{left:441px;top:222px;width:169px;height:52px;border:2px solid;border-image:linear-gradient(90deg,var(--violet),var(--blue)) 1}
.services-label{position:absolute;left:44px;top:-9px;width:80px;height:16px;background:var(--label);text-align:center;font-weight:900;font-size:15.5px;line-height:16px;color:var(--violet)}
.services-list{position:absolute;left:5px;top:10px;display:grid;grid-template-columns:87px 80px;grid-auto-flow:column;grid-template-rows:repeat(4,9px);font-size:5.6px;font-weight:700;text-transform:uppercase}
.services-list li{list-style:none;white-space:nowrap}
.services-list li::before{content:"✓ ";font-size:5px}

/* inside */
.inside-title{left:0;width:222px;top:28px;text-align:center;font-weight:900;font-size:35px;letter-spacing:.5px}
.divider{position:absolute;height:2px;background:linear-gradient(90deg,transparent,var(--magenta) 50%,transparent)}
.service-photo{position:absolute;width:71px;height:75px;clip-path:polygon(0 0,76% 0,100% 100%,0 100%)}
.service{position:absolute;width:135px}
.service h3{font-weight:700;font-size:9.6px;color:var(--magenta);line-height:11px;text-transform:uppercase}
.service ul{margin-top:1px}
.service li{list-style:none;font-size:4.6px;line-height:10.3px;text-transform:uppercase;letter-spacing:.2px}
.service li::before{content:"• "}
.service li.wrap{line-height:10.3px}
</style>
</head>
<body>

<!-- OUTSIDE -->
<section class="sheet sheet--outside">
  <div class="panel panel--1"></div>
  <div class="panel panel--2"></div>
  <div class="panel panel--3"></div>
  <svg class="art" width="633" height="448" viewBox="0 0 633 448">
    <defs>
      <linearGradient id="arcGrad" x1="0" y1="0" x2="1" y2="0">
        <stop offset="0" stop-color="#d21fe8"/><stop offset=".6" stop-color="#e52bd6"/><stop offset="1" stop-color="#9b3ff0"/>
      </linearGradient>
      <linearGradient id="domeGrad" x1="0" y1="1" x2="1" y2="0">
        <stop offset="0" stop-color="#a23ff0"/><stop offset="1" stop-color="#4ba9f2"/>
      </linearGradient>
      <linearGradient id="washPhoto" x1="0" y1="0" x2="1" y2="1">
        <stop offset="0" stop-color="#5a5d63"/><stop offset=".5" stop-color="#c9c9cc"/><stop offset="1" stop-color="#d9a58d"/>
      </linearGradient>
      <linearGradient id="polishPhoto" x1="0" y1="0" x2="1" y2="0">
        <stop offset="0" stop-color="#bfc7c4"/><stop offset=".25" stop-color="#3aa8a6"/><stop offset=".45" stop-color="#2a2b2e"/><stop offset=".75" stop-color="#2a2b2c"/><stop offset="1" stop-color="#55524f"/>
      </linearGradient>
    </defs>
    <path d="M2,448 L2,405 A104,104 0 0 1 211,395 L211,448 Z" fill="url(#washPhoto)" role="img" aria-label="Photo of a wheel being cleaned with a brush and foam"/>
    <path d="M1,448 L1,420 A104,104 0 0 1 211,398" fill="none" stroke="url(#domeGrad)" stroke-width="6"/>
    <path d="M211,186 A234,234 0 0 0 633,262 L633,448 L211,448 Z" fill="url(#polishPhoto)" role="img" aria-label="Photo of a car interior being polished with a machine polisher"/>
    <path d="M211,186 A234,234 0 0 0 633,262" fill="none" stroke="url(#arcGrad)" stroke-width="7"/>
  </svg>

  <div class="abs mini-brand"><div class="ring"></div><p>VELVET<br>CREST</p></div>
  <h2 class="abs about-title">ABOUT US</h2>
  <p class="abs about-text">The ultimate destination for car care in Geneva. We provide personalized, detail-oriented services that bring out the best in your car. With our expert techniques and dedicated approach, we ensure that your car receives the utmost care and attention. Experience a place where passion meets precision and let us create an exceptional car care experience designed just for you.</p>

  <ul class="abs contact">
    <li><svg viewBox="0 0 10 10"><path d="M2 1 L4 1 L4.6 3 L3.4 4 Q4.5 6 6 6.6 L7 5.4 L9 6 L9 8 Q5 9 2 5 Q1 3 2 1Z" fill="var(--magenta)"/></svg>000 000 0000</li>
    <li><svg viewBox="0 0 10 10" fill="none" stroke="var(--magenta)" stroke-width=".8"><circle cx="5" cy="5" r="4"/><ellipse cx="5" cy="5" rx="1.8" ry="4"/><path d="M1 5h8M2 3h6M2 7h6"/></svg>www.website.com</li>
    <li><svg viewBox="0 0 10 10"><rect x="1" y="1" width="8" height="8" rx="2" fill="none" stroke="var(--magenta)" stroke-width="1"/></svg>@velvetcrest</li>
  </ul>
  <div class="abs address"><svg viewBox="0 0 10 12"><path d="M5 0.5 A4 4 0 0 1 9 4.5 C9 7.5 5 11.5 5 11.5 C5 11.5 1 7.5 1 4.5 A4 4 0 0 1 5 0.5Z" fill="var(--magenta)"/><circle cx="5" cy="4.5" r="1.5" fill="var(--black)"/></svg><p>0000 Street<br>Address<br>0000</p></div>
  <div class="abs hours"><h3>OPENING HOURS</h3><p>09:00-17:00</p></div>

  <div class="abs brand"><div class="ring"></div><p>VELVET<br>CREST</p></div>
  <div class="abs services-box">
    <div class="services-label">SERVICES</div>
    <ul class="services-list">
      <li>Detailing &amp; hand wash</li><li>Polishing</li><li>Ceramic treatment</li><li>Dry ice wash</li>
      <li>Covering</li><li>Protection film</li><li>Detailing boutique</li>
    </ul>
  </div>
</section>

<!-- INSIDE -->
<section class="sheet sheet--inside">
  <div class="panel panel--1"></div>
  <div class="panel panel--2"></div>
  <div class="panel panel--3"></div>
  <svg class="art" width="633" height="448" viewBox="0 0 633 448">
    <defs>
      <linearGradient id="titleArc" x1="0" y1="0" x2="1" y2="0">
        <stop offset="0" stop-color="#d21fe8"/><stop offset=".7" stop-color="#e32bd8"/><stop offset="1" stop-color="#9b46f0"/>
      </linearGradient>
    </defs>
    <path d="M6,0 A118,118 0 0 0 211,88" fill="none" stroke="url(#titleArc)" stroke-width="5"/>
  </svg>
  <h2 class="abs inside-title">SERVICES</h2>

  <div class="divider" style="left:12px;top:178px;width:190px"></div>
  <div class="divider" style="left:12px;top:308px;width:190px"></div>
  <div class="divider" style="left:221px;top:158px;width:190px"></div>
  <div class="divider" style="left:221px;top:284px;width:190px"></div>
  <div class="divider" style="left:438px;top:244px;width:190px"></div>

  <div class="service-photo" style="left:0;top:207px;background:linear-gradient(135deg,#4a5a9a,#c8cde0 50%,#2a2a2e)" role="img" aria-label="Photo of a wash mitt on a car"></div>
  <div class="service" style="left:77px;top:210px">
    <h3>Detailing &amp; Hand Wash</h3>
    <ul><li>Comprehensive exterior &amp; interior care</li><li class="wrap">Personalisation and tailored cleaning<br>&nbsp;&nbsp;packages</li><li>Decontamination</li><li>Premium products</li><li>Attention to detail for a perfect finish</li></ul>
  </div>

  <div class="service-photo" style="left:0;top:326px;background:linear-gradient(135deg,#3b3b3f,#2d7fb0 40%,#1a1a1c 70%,#2a9c7a)" role="img" aria-label="Photo of a machine polisher on paint"></div>
  <div class="service" style="left:77px;top:334px">
    <h3>Polishing</h3>
    <ul><li>Eliminates scratches, holograms</li><li>Revives and protects paint</li><li>Ensures lasting gloss</li><li>Enhances paint life</li><li>Preserves car’s value and beauty</li></ul>
  </div>

  <div class="service-photo" style="left:211px;top:61px;background:linear-gradient(135deg,#8a0f12,#e02020 45%,#f0d0d0 75%,#b01818)" role="img" aria-label="Photo of glossy red paint after ceramic treatment"></div>
  <div class="service" style="left:294px;top:70px">
    <h3>Ceramic Treatment</h3>
    <ul><li>Durable paint protection</li><li>Water-repellent (hydrophobic) effect</li><li>Easier cleaning, enhanced shine</li><li>Long-term surface safeguarding</li><li>Shields against environmental impacts</li></ul>
  </div>

  <div class="service-photo" style="left:211px;top:191px;background:linear-gradient(135deg,#e8e8ea,#b0b4b8 45%,#2a2a2c)" role="img" aria-label="Photo of a dry ice cleaning machine"></div>
  <div class="service" style="left:294px;top:195px">
    <h3>Dry Ice Wash</h3>
    <ul><li>Innovative, waterless method</li><li>Safe for all car parts</li><li>Deep cleans, removes odors</li><li>Allergen-free, antibacterial</li><li>Gentle, effective</li><li>Advanced cleaning technology</li></ul>
  </div>

  <div class="service-photo" style="left:211px;top:298px;background:linear-gradient(135deg,#f2f2f4,#c9cbd0 45%,#3c4150)" role="img" aria-label="Photo of a vehicle being wrapped with film"></div>
  <div class="service" style="left:294px;top:303px">
    <h3>Covering</h3>
    <ul><li>Personalized vehicle styling</li><li>More than 150 colours available</li><li>Clean cut without using a cutter</li><li>High-quality, durable materials</li><li>Custom designs available</li></ul>
  </div>

  <div class="service-photo" style="left:422px;top:136px;background:linear-gradient(135deg,#6c6e72,#d9d34a 40%,#1d1d20 75%,#8a8c90)" role="img" aria-label="Photo of protection film being applied with a squeegee"></div>
  <div class="service" style="left:500px;top:150px">
    <h3>Protection Film</h3>
    <ul><li>Invisible, durable shield</li><li>Self-healing technology</li><li>10-year warranty by QR VONT</li></ul>
  </div>

  <div class="service-photo" style="left:422px;top:272px;background:linear-gradient(135deg,#6a6c72,#f07a20 45%,#1a1a1c)" role="img" aria-label="Photo of care products on an orange microfibre towel"></div>
  <div class="service" style="left:500px;top:277px">
    <h3>Detailing Boutique</h3>
    <ul><li>Premium brands available</li><li>Buy on site during your visit</li><li>Marble Harbour, Zeb Autos, DRUP Polaro</li><li>Essential for at-home car care</li><li>Perfect for quick touch-ups</li></ul>
  </div>
</section>

</body>
</html>
```